3 Business Card designs for a company with multiple services

We are a company that has 3 main services:

1) Security - CCTV & Alarm Sepcialists
2) Broadcast - Broadcast Sales and Technical Services
3) Distribution - Quality Products, Quality Service

The broadcast service is for Video Broadcast.

I will include our logos for each service.

I would like to also create a business card design for 7QK in general (see main logo).

Each card will be two-sided. On the front I would think it would include Logo, Name, Posistion and Mobile (and possibly email). And possibly our main number (which may be something like 1800 639 415)

On the back it MUST include a "lined" section to be able to write short quotes / prices.

Then include more details like Phone: 1800 639 415 Fax: 1800 639 412 Postal: PO Box 731, Tallowen, QLD Australia 4290 Website: www.7qk.com.au

We would like a fresh, inovative card design with that "wow check this out" feel about it.

Look forward to seeing what you can do! :)

Corey

Industry/Entity Type

Business

Requirements
Must have
• Quote section on the back!
Editable files.

```html
<!DOCTYPE html>
<html lang="en">
<head>
<meta charset="utf-8">
<title>7QK Business Cards</title>
<link rel="stylesheet" href="https://fonts.googleapis.com/css2?family=Arimo:wght@400;700&display=swap">
<style>
:root{
  --page:#ffffff;
  --ink:#222222;
  --muted:#8a8a8a;
  --white:#ffffff;
  --black-card:#050505;
  --black-hi:#3a3a3a;
  --grey-card:#75777b;
  --grey-hi:#c9cacc;
  --orange-card:#d27a1f;
  --orange-hi:#f2a23a;
  --blue-card:#1f3a8f;
  --blue-hi:#2a8fd6;
  --accent-red:#e0242a;
  --accent-gold:#e9b33b;
}
*{margin:0;padding:0;box-sizing:border-box}
html,body{width:1200px;height:900px;overflow:hidden;background:var(--page)}
body{position:relative;font-family:"Arimo",Arial,sans-serif;color:var(--ink)}
.card{position:absolute;overflow:hidden;box-shadow:4px 5px 6px rgba(0,0,0,.45)}
.card--front-main{left:158px;top:100px;width:387px;height:212px;
  background:radial-gradient(ellipse at 100% 100%,var(--black-hi) 0%,var(--black-card) 40%)}
.card--back{left:668px;top:100px;width:388px;height:210px;background:var(--white);border:1px solid #555}
.card--vertical{top:417px;width:210px;height:386px}
.card--security{left:158px;background:radial-gradient(ellipse at 100% 100%,var(--grey-hi) 0%,var(--grey-card) 45%)}
.card--broadcast{left:494px;background:radial-gradient(ellipse at 100% 100%,var(--orange-hi) 0%,var(--orange-card) 45%)}
.card--distribution{left:846px;background:radial-gradient(ellipse at 100% 100%,var(--blue-hi) 0%,var(--blue-card) 45%)}

.icon-slot{position:absolute;border-radius:4px}
.logo{position:absolute;display:flex;align-items:center;gap:10px;
  color:var(--white);font-weight:700;letter-spacing:.3em;white-space:nowrap}
.logo__mark{width:9px;height:9px;background:var(--white)}

.card--front-main .logo{left:206px;top:14px;height:50px;font-size:32px}
.tagline{position:absolute;left:0;right:0;top:70px;text-align:center;color:var(--white);
  font-weight:700;font-size:14px;letter-spacing:.08em;white-space:nowrap}
.main-details{position:absolute;left:12px;right:12px;top:172px;display:flex;justify-content:space-between;
  color:var(--white);font-size:12px;line-height:18px}
.main-details .right{text-align:right}

.card--vertical .logo{left:80px;top:4px;height:40px;font-size:24px}
.service-label{position:absolute;right:10px;top:52px;color:var(--white);font-weight:700;font-size:12px;letter-spacing:.28em;white-space:nowrap}
.contact{position:absolute;left:0;right:0;top:214px;text-align:center;color:var(--white);font-size:12px;line-height:18px}
.contact .role{margin-bottom:18px}
.contact .key{font-size:8px;font-weight:700;line-height:18px}
.card--security .key{color:var(--accent-red)}
.card--broadcast .key{color:#7a5a2a}
.card--distribution .key{color:var(--accent-gold)}

.appointment__title{position:absolute;left:0;right:0;top:2px;text-align:center;font-weight:700;font-size:16px;letter-spacing:.22em}
.appointment__row{position:absolute;left:21px;right:18px;display:flex;align-items:flex-end;font-size:16px}
.appointment__row span{width:72px}
.appointment__row i{flex:1;border-bottom:1px solid var(--ink);height:1px;margin-bottom:4px}
.appointment__note{position:absolute;left:16px;right:16px;top:114px;text-align:center;color:var(--muted);font-size:11px;line-height:15px}
.appointment__info{position:absolute;left:0;right:0;top:151px;text-align:center;font-size:11px;line-height:16px}
.appointment__info b{color:var(--muted);font-weight:400}
</style>
</head>
<body>

<section class="card card--front-main">
  <div class="icon-slot" role="img" aria-label="Padlock icon for security" style="left:22px;top:16px;width:36px;height:40px;background:#8d8d8d"></div>
  <div class="icon-slot" role="img" aria-label="Broadcast camera icon" style="left:70px;top:18px;width:56px;height:36px;background:#e0932a"></div>
  <div class="icon-slot" role="img" aria-label="Globe icon for distribution" style="left:140px;top:16px;width:40px;height:40px;border-radius:50%;background:#2a6fc2"></div>
  <div class="logo"><span>7QK</span><span class="logo__mark"></span></div>
  <div class="tagline">SECURITY - BROADCAST - DISTRIBUTION</div>
  <div class="main-details">
    <div>Persons Name<br>DIRECTOR</div>
    <div class="right">04198765432<br>Name@7qk.com.au</div>
  </div>
</section>

<section class="card card--back">
  <div class="appointment__title">APPOINTMENT</div>
  <div class="appointment__row" style="top:34px"><span>DATE :</span><i></i></div>
  <div class="appointment__row" style="top:58px"><span>TIME:</span><i></i></div>
  <div class="appointment__row" style="top:80px"><span>PLACE:</span><i></i></div>
  <p class="appointment__note">If you are unable to attend the appointment please notify me<br>as soon as possible.</p>
  <p class="appointment__info"><b>T</b> 1800 639 415 &nbsp;<b>F</b> 1800 639 412<br>PO Box 731, Tallowen, QLD Australia 4290<br>www.7qk.com.au</p>
</section>

<section class="card card--vertical card--security">
  <div class="icon-slot" role="img" aria-label="Red padlock icon" style="left:14px;top:8px;width:36px;height:42px;background:var(--accent-red)"></div>
  <div class="logo"><span>7QK</span><span class="logo__mark"></span></div>
  <div class="service-label">SECURITY</div>
  <div class="contact">
    <div>Persons Name</div><div class="role">DIRECTOR</div>
    <div class="key">M</div><div>04198765432</div>
    <div class="key">E</div><div>Name@7qk.com.au</div>
    <div class="key">T</div><div>1800 639 415</div>
  </div>
</section>

<section class="card card--vertical card--broadcast">
  <div class="icon-slot" role="img" aria-label="Broadcast camera icon" style="left:4px;top:0;width:64px;height:52px;background:linear-gradient(135deg,#f4c020,#2d5aa0)"></div>
  <div class="logo"><span>7QK</span><span class="logo__mark"></span></div>
  <div class="service-label">BROADCAST</div>
  <div class="contact">
    <div>Persons Name</div><div class="role">DIRECTOR</div>
    <div class="key">M</div><div>04198765432</div>
    <div class="key">E</div><div>Name@7qk.com.au</div>
    <div class="key">T</div><div>1800 639 415</div>
  </div>
</section>

<section class="card card--vertical card--distribution">
  <div class="icon-slot" role="img" aria-label="Globe icon" style="left:8px;top:6px;width:48px;height:48px;border-radius:50%;background:radial-gradient(circle at 40% 40%,#f2d27a,#2a6fc2 65%)"></div>
  <div class="logo"><span>7QK</span><span class="logo__mark"></span></div>
  <div class="service-label">DISTRIBUTION</div>
  <div class="contact">
    <div>Persons Name</div><div class="role">DIRECTOR</div>
    <div class="key">M</div><div>04198765432</div>
    <div class="key">E</div><div>Name@7qk.com.au</div>
    <div class="key">T</div><div>1800 639 415</div>
  </div>
</section>

</body>
</html>
```